Design a graphic that shows who we are

We're looking for an experienced graphic designer to help us redesign a pivotal infographic that represents our company's purpose, vision, strategic objectives, and core values.
The existing design, which can be found in the attached files, is currently in the shape of a pyramid, symbolizing that our core values are the pillars of our existence or our foundation. While we appreciate this symbolism, it's not a strict requirement for the redesign. We're primarily interested in an update that will make the graphic more professional and eye-catching, without changing the content (slightly flexible on this).
This graphic will be used extensively in firm presentations, on our website, and across our marketing materials, so the design's impact will be far-reaching. We're eager to see how you might interpret and refresh this crucial visual representation of our company.
Target Market(s)
Mid-market businesses ($50m+), Executives, High net worth individuals, Professional Service Providers, Employment candidates (Gen Z & Millenials mostly), Referral sources (bankers, investment brokers, insurance providers, etc.)
Industry/Entity Type
Business, Accounting, Tax, Finance
Look and feel

```html
<!DOCTYPE html>
<html lang="en">
<head>
<meta charset="UTF-8">
<title>Fundamental Pillars of H+F</title>
<link href="https://fonts.googleapis.com/css2?family=Roboto:wght@400;500;700;900&display=swap" rel="stylesheet">
<style>
  :root {
    --navy: #1a469f;
    --navy-deep: #102c66;
    --gold: #d4a862;
    --gold-soft: #e8cf9f;
    --stone: #e6e9ef;
    --stone-dark: #d5dae3;
    --ink: #646a75;
    --ink-strong: #3e4450;
    --paper: #ffffff;
    --mist: #f5f7fa;
  }
  * { margin: 0; padding: 0; box-sizing: border-box; }
  html, body { width: 1200px; height: 848px; overflow: hidden; background: var(--paper); }
  body { position: relative; font-family: "Roboto", Arial, sans-serif; }

  .temple { position: absolute; left: 0; top: 0; width: 1200px; height: 848px; }

  .brand {
    position: absolute; left: 0; width: 1200px; top: 86px;
    display: flex; justify-content: center; align-items: center; gap: 10px;
  }
  .brand-name { font-size: 22px; font-weight: 500; color: var(--gold); letter-spacing: 1px; }
  .brand-mark { width: 12px; height: 12px; background: var(--gold); }

  .title {
    position: absolute; left: 0; width: 1200px; top: 140px;
    text-align: center; color: var(--paper);
    font-size: 46px; font-weight: 900; line-height: 54px; letter-spacing: 1px;
  }

  .value-badge {
    position: absolute; width: 80px; height: 80px; margin-left: -40px; top: 366px;
    border-radius: 50%; background: var(--navy);
    border: 3px solid var(--paper);
    box-shadow: 0 0 0 2px var(--gold), 0 8px 18px rgba(16, 44, 102, 0.28);
    display: flex; align-items: center; justify-content: center;
  }
  .value-badge svg { width: 44px; height: 44px; }
  .value-name {
    position: absolute; width: 180px; margin-left: -90px; top: 462px;
    text-align: center; color: var(--navy-deep);
    font-size: 23px; font-weight: 900; letter-spacing: 0.2px;
  }

  .foundation {
    position: absolute; left: 40px; top: 652px; width: 1120px; height: 176px;
    display: flex; gap: 20px;
  }
  .foundation-card {
    flex: 1; background: var(--paper);
    border-top: 4px solid var(--gold);
    border-radius: 4px;
    box-shadow: 0 6px 20px rgba(16, 44, 102, 0.12);
    padding: 16px 22px 0;
    text-align: center;
  }
  .block-heading {
    display: flex; align-items: center; justify-content: center; gap: 10px;
    height: 28px;
    color: var(--navy); font-size: 19px; font-weight: 700; letter-spacing: 0.6px;
  }
  .block-text { margin-top: 14px; color: var(--ink); font-size: 15px; line-height: 20px; }
  .block-text strong { color: var(--ink-strong); font-weight: 700; }
  .purpose .block-text { margin-top: 26px; }
</style>
</head>
<body>

<svg class="temple" viewBox="0 0 1200 848" aria-hidden="true">
  <defs>
    <linearGradient id="roofFill" x1="0" y1="0" x2="0" y2="1">
      <stop offset="0" stop-color="#1f52b5"/>
      <stop offset="1" stop-color="#102c66"/>
    </linearGradient>
    <linearGradient id="shaftFill" x1="0" y1="0" x2="1" y2="0">
      <stop offset="0" stop-color="#d5dae3"/>
      <stop offset="0.45" stop-color="#eef1f5"/>
      <stop offset="1" stop-color="#d5dae3"/>
    </linearGradient>
    <linearGradient id="groundFade" x1="0" y1="0" x2="0" y2="1">
      <stop offset="0" stop-color="#eef1f6"/>
      <stop offset="1" stop-color="#ffffff"/>
    </linearGradient>
  </defs>

  <rect x="0" y="632" width="1200" height="216" fill="url(#groundFade)"/>

  <polygon points="600,22 1060,180 140,180" fill="url(#roofFill)"/>
  <rect x="170" y="180" width="860" height="80" fill="var(--navy-deep)"/>
  <rect x="170" y="260" width="860" height="4" fill="var(--gold)"/>

  <g>
    <g transform="translate(220 0)">
      <rect x="-46" y="272" width="92" height="10" fill="var(--stone-dark)"/><rect x="-36" y="285" width="72" height="5" fill="var(--stone-dark)"/>
      <rect x="-30" y="292" width="60" height="298" fill="url(#shaftFill)"/>
      <rect x="-36" y="592" width="72" height="5" fill="var(--stone-dark)"/><rect x="-46" y="600" width="92" height="12" fill="var(--stone-dark)"/>
    </g>
    <g transform="translate(410 0)">
      <rect x="-46" y="272" width="92" height="10" fill="var(--stone-dark)"/><rect x="-36" y="285" width="72" height="5" fill="var(--stone-dark)"/>
      <rect x="-30" y="292" width="60" height="298" fill="url(#shaftFill)"/>
      <rect x="-36" y="592" width="72" height="5" fill="var(--stone-dark)"/><rect x="-46" y="600" width="92" height="12" fill="var(--stone-dark)"/>
    </g>
    <g transform="translate(600 0)">
      <rect x="-46" y="272" width="92" height="10" fill="var(--stone-dark)"/><rect x="-36" y="285" width="72" height="5" fill="var(--stone-dark)"/>
      <rect x="-30" y="292" width="60" height="298" fill="url(#shaftFill)"/>
      <rect x="-36" y="592" width="72" height="5" fill="var(--stone-dark)"/><rect x="-46" y="600" width="92" height="12" fill="var(--stone-dark)"/>
    </g>
    <g transform="translate(790 0)">
      <rect x="-46" y="272" width="92" height="10" fill="var(--stone-dark)"/><rect x="-36" y="285" width="72" height="5" fill="var(--stone-dark)"/>
      <rect x="-30" y="292" width="60" height="298" fill="url(#shaftFill)"/>
      <rect x="-36" y="592" width="72" height="5" fill="var(--stone-dark)"/><rect x="-46" y="600" width="92" height="12" fill="var(--stone-dark)"/>
    </g>
    <g transform="translate(980 0)">
      <rect x="-46" y="272" width="92" height="10" fill="var(--stone-dark)"/><rect x="-36" y="285" width="72" height="5" fill="var(--stone-dark)"/>
      <rect x="-30" y="292" width="60" height="298" fill="url(#shaftFill)"/>
      <rect x="-36" y="592" width="72" height="5" fill="var(--stone-dark)"/><rect x="-46" y="600" width="92" height="12" fill="var(--stone-dark)"/>
    </g>
  </g>

  <rect x="130" y="612" width="940" height="16" fill="var(--navy-deep)"/>
  <rect x="130" y="628" width="940" height="3" fill="var(--gold)"/>
</svg>

<div class="brand">
  <span class="brand-mark"></span>
  <span class="brand-name">Harlow Finch LLP</span>
</div>

<h1 class="title">FUNDAMENTAL PILLARS<br>OF H+F (OUR VALUES)</h1>

<div class="value-badge" style="left:220px">
  <svg viewBox="0 0 44 44"><circle cx="17" cy="17" r="9.5" fill="none" stroke="var(--gold)" stroke-width="4.5"/><line x1="24.5" y1="24.5" x2="36" y2="34" stroke="var(--gold)" stroke-width="6" stroke-linecap="round"/></svg>
</div>
<div class="value-name" style="left:220px">Accountable</div>

<div class="value-badge" style="left:410px">
  <svg viewBox="0 0 44 44"><path d="M22 20 C14 14 14 6 19 6 C21 6 22 8 22 9 C22 8 23 6 25 6 C30 6 30 14 22 20Z" fill="var(--gold)"/><rect x="5" y="25" width="5" height="11" fill="var(--gold)"/><path d="M11 26 H20 C23 26 24 29 21 29 H16 H23 L35 25 C38 24 39 27 37 28 L25 35 H11Z" fill="var(--gold)"/></svg>
</div>
<div class="value-name" style="left:410px">Caring</div>

<div class="value-badge" style="left:600px">
  <svg viewBox="0 0 44 44"><text x="22" y="32" text-anchor="middle" font-family="Roboto, Arial, sans-serif" font-weight="900" fill="var(--gold)"><tspan font-size="18">?</tspan><tspan font-size="28">?</tspan><tspan font-size="18">?</tspan></text></svg>
</div>
<div class="value-name" style="left:600px">Curious</div>

<div class="value-badge" style="left:790px">
  <svg viewBox="0 0 44 44"><path d="M22 10 C16 10 14 15 15 19 C16 23 19 25 19 29 H25 C25 25 28 23 29 19 C30 15 28 10 22 10Z" fill="var(--gold)"/><rect x="19" y="30" width="6" height="2" fill="var(--gold)"/><rect x="19" y="33" width="6" height="2" fill="var(--gold)"/><rect x="20" y="36" width="4" height="2" fill="var(--gold)"/><g stroke="var(--gold)" stroke-width="1.2" stroke-linecap="round"><line x1="22" y1="3" x2="22" y2="6"/><line x1="13" y1="7" x2="15" y2="9"/><line x1="31" y1="7" x2="29" y2="9"/><line x1="9" y1="15" x2="12" y2="16"/><line x1="35" y1="15" x2="32" y2="16"/></g></svg>
</div>
<div class="value-name" style="left:790px">Innovative</div>

<div class="value-badge" style="left:980px">
  <svg viewBox="0 0 44 44"><g fill="var(--gold)"><rect x="4" y="10" width="6" height="12" transform="rotate(-40 7 16)"/><rect x="34" y="10" width="6" height="12" transform="rotate(40 37 16)"/><path d="M11 18 L19 12 L26 14 L33 20 L25 30 L18 26 Z"/><circle cx="14" cy="27" r="2"/><circle cx="17" cy="30" r="2"/><circle cx="20" cy="33" r="2"/><circle cx="23" cy="35" r="2"/></g></svg>
</div>
<div class="value-name" style="left:980px">Collaborative</div>

<div class="foundation">
  <section class="foundation-card purpose">
    <h2 class="block-heading">
      <svg width="26" height="26" viewBox="0 0 27 27" aria-hidden="true"><circle cx="13.5" cy="13.5" r="11.5" fill="none" stroke="var(--navy)" stroke-width="2.6"/><circle cx="13.5" cy="13.5" r="6.5" fill="none" stroke="var(--navy)" stroke-width="2.6"/><circle cx="13.5" cy="13.5" r="2.6" fill="var(--navy)"/></svg>
      PURPOSE
    </h2>
    <p class="block-text">At H+F, we strive to provide exceptional tax, assurance and advisory services to our clients to assist them in achieving their goals.</p>
  </section>

  <section class="foundation-card vision">
    <h2 class="block-heading">
      <svg width="40" height="20" viewBox="0 0 48 24" aria-hidden="true"><path d="M1 12 C10 -2 38 -2 47 12 C38 26 10 26 1 12Z" fill="var(--navy)"/><circle cx="24" cy="12" r="7" fill="var(--paper)"/></svg>
      VISION
    </h2>
    <p class="block-text">To empower our team members to reach their highest potential. To be our client’s go&#8209;to trusted business advisor and strategic partner. To be united with a One Firm Culture and live and breathe our core values.</p>
  </section>

  <section class="foundation-card objectives">
    <h2 class="block-heading">
      <svg width="28" height="24" viewBox="0 0 32 26" aria-hidden="true"><rect x="1" y="4" width="21" height="21" fill="none" stroke="var(--navy)" stroke-width="1.8"/><path d="M5 13 L11 20 L30 2" fill="none" stroke="var(--navy)" stroke-width="4.5"/></svg>
      STRATEGIC OBJECTIVES
    </h2>
    <p class="block-text" style="line-height:19px">
      <strong>Build</strong> Service Partnerships<br>
      <strong>Embrace</strong> a One Firm Culture<br>
      <strong>Remain</strong> an independent CPA Firm<br>
      <strong>Be</strong> a proactive and creative CPA firm<br>
      <strong>Cultivate</strong> a “People First” work environment
    </p>
  </section>
</div>

</body>
</html>
```